New look and feel for investment website

Hi

Our website needs a crisp and professional look and feel applying to it. Here’s the address: http://www.plumbvane.co.uk. Since posting the brief yesterday (Tuesday, 16 August), we've reduced the amount of content on the home page, which should make life a little easier for you. We will come back later today, with some points of reference in terms of sites we like the look of. (See below)

17 August, 1.20pm GMT. OK, comments generally on the designs submitted so far. Please keep in mind that images of graphs, piles of coins, paper money and pretty females are not what is required. Better to think in terms of abstract imagery instead. Ratios? Circles? Relationships? Patterns? Not money,sex,graphs etc. Hope that helps.

For guidance on look and feel, please refer to these sites, which we like:

http://www.belmorrow.co.uk/
http://www.qv.com/
https://www.tolverhampsley.com
https://www.marigatefunds.com
https://www.pkalune.com
Updates

Here's the Tern Harbor logo created in AI CS5.

Our market is professional financial advisers and relatively sophisticated private investors. The look and feel therefore should be slick and sophisticated - not 'lively' and lightweight, more like a banking site. Please read the brief again where we've added a list of websites that we really like the look of to get a better feel for what we're looking for. Thanks once again, we appreciate the work you're putting in.

It's essential that all the elements that are on the current home page be included on all new designs. 

We use a device in our e-mails which you may wish to incorporate in your design.

Target Market(s)

Professional financial advisers. People who know about investment and money.

Industry/Entity Type

Investment

Requirements
Should not have
• Graphs or people.

```html
<!DOCTYPE html>
<html lang="en">
<head>
<meta charset="utf-8">
<title>Tern Harbor — Home</title>
<link rel="stylesheet" href="https://fonts.googleapis.com/css2?family=Arimo:ital,wght@0,400;0,700;1,400&display=swap">
<style>
:root{
  --page-top:#c9d0d2;
  --page-bottom:#9aa6aa;
  --ink:#222222;
  --ink-soft:#333333;
  --brand-dark:#2a2a2a;
  --brand-red:#d6252b;
  --nav-top:#3a3a3a;
  --nav-bottom:#141414;
  --panel:#e4e6e7;
  --side-top:#f6b545;
  --side-bottom:#e4920e;
  --side-active:#2e2e2e;
  --trial-top:#3fa3e0;
  --trial-bottom:#1b78c0;
  --white:#ffffff;
  --tab:#dfe3e4;
  --search-field:#c9d3d6;
}
*{box-sizing:border-box;margin:0;padding:0}
html,body{width:1200px;height:900px;overflow:hidden}
body{
  position:relative;
  font-family:"Arimo",Arial,sans-serif;
  color:var(--ink);
  background:radial-gradient(ellipse at 45% 35%,#dde2e3 0%,var(--page-top) 45%,var(--page-bottom) 100%);
}
.backdrop{position:absolute;inset:0;background:linear-gradient(180deg,rgba(255,255,255,.15),rgba(0,0,0,.05))}

.brand{position:absolute;left:141px;top:14px}
.brand-name{font-size:42px;font-weight:400;color:var(--brand-dark);letter-spacing:-1px;line-height:1;white-space:nowrap}

.contact-tab{position:absolute;left:725px;top:0;width:334px;height:25px;background:var(--tab);
  border-radius:0 0 4px 4px;display:flex;align-items:center;font-size:12px;color:var(--ink-soft);white-space:nowrap}
.contact-tab span{display:flex;align-items:center;gap:6px;padding:0 10px;height:100%;white-space:nowrap}
.contact-tab span+span{border-left:1px solid #b9bfc1}

.nav{position:absolute;left:141px;top:68px;width:918px;height:42px;
  background:linear-gradient(var(--nav-top),var(--nav-bottom));border-radius:8px 8px 0 0;
  display:flex;align-items:center;color:var(--white);font-size:12px;font-weight:700}
.nav-home{width:46px;height:100%;display:flex;align-items:center;justify-content:center;border-right:1px solid #4a4a4a}
.nav-links{display:flex;gap:7px;padding-left:11px}
.nav-links a{color:var(--white);text-decoration:none}
.nav-links i{font-style:normal;color:#bbb}
.follow{margin-left:auto;display:flex;align-items:center;gap:6px;font-weight:400}
.social{width:20px;height:20px;border-radius:3px;background:#5b9ad0;display:inline-block}
.social+.social{background:#3a5f9e}
.search{display:flex;margin:0 8px 0 14px}
.search-field{width:141px;height:22px;background:var(--search-field);border:1px solid #9aa;border-radius:3px 0 0 3px}
.search-btn{width:60px;height:22px;background:linear-gradient(#fff,#d8dde0);border:1px solid #9aa;border-left:0;
  border-radius:0 3px 3px 0;color:#1a3d7a;font-size:11px;font-weight:700;display:flex;align-items:center;justify-content:center}

.hero{position:absolute;left:141px;top:110px;width:918px;height:202px;
  background:linear-gradient(100deg,#0c0505 0%,#160606 45%,#5a0a0e 70%,#a0141b 85%,#3a0608 100%)}
.hero-title{position:absolute;left:27px;top:34px;width:570px;font-size:23px;line-height:28px;color:var(--white);font-weight:400}
.hero-cta{position:absolute;left:27px;top:139px;width:185px;height:38px;
  background:linear-gradient(#e2474a,#b8191e);border-radius:4px 0 0 4px;
  clip-path:polygon(0 0,92% 0,100% 50%,92% 100%,0 100%);
  color:var(--white);font-weight:700;font-size:13px;display:flex;align-items:center;padding-left:23px;letter-spacing:.3px}

.content{position:absolute;left:141px;top:312px;width:918px;height:449px;background:var(--panel)}

.sidebar{position:absolute;left:146px;top:318px;width:206px;height:360px;
  background:linear-gradient(var(--side-top),var(--side-bottom));border:1px solid #d88a10;padding-top:5px}
.sidebar ul{list-style:none}
.sidebar li{font-size:11.5px;font-weight:700;color:#2a2210;padding:0 10px;line-height:14px;margin-bottom:13px}
.sidebar li.active{background:var(--side-active);color:var(--white);height:24px;line-height:24px;margin:0 10px 10px 0;
  clip-path:polygon(0 0,94% 0,100% 50%,94% 100%,0 100%)}
.trial{position:absolute;left:145px;top:683px;width:206px;height:72px;
  background:linear-gradient(var(--trial-top),var(--trial-bottom));border:2px solid #8cc7ee;border-radius:3px;
  color:var(--white);font-size:11.5px;font-weight:700;line-height:13.5px;padding:7px 9px}
.rule-v{position:absolute;left:356px;top:318px;width:1px;height:437px;background:#bfc3c4}

.intro-title{position:absolute;left:370px;top:320px;width:590px;color:var(--brand-red);font-size:17px;font-weight:700;line-height:20px}
.intro-image{position:absolute;left:367px;top:367px;width:175px;height:198px;border:1px solid #c0c4c6;background:#f4f5f5;padding:5px}
.intro-image div{width:100%;height:100%;background:linear-gradient(160deg,#dfe9f3 0%,#7fa5cf 40%,#2f5b92 75%,#1d3c66 100%)}
.intro-text{position:absolute;left:549px;top:367px;width:490px;font-size:11.5px;line-height:13.8px;color:var(--ink-soft)}
.intro-text p+p{margin-top:14px}
.intro-text .lead{font-weight:700;margin-top:10px}
.rule-h{position:absolute;left:365px;top:584px;width:687px;height:1px;background:#a9adae}

.stats{position:absolute;left:366px;top:597px;display:flex;gap:7px}
.stat{width:130px}
.stat-image{height:88px;border:1px solid #c0c4c6;background:#f4f5f5;padding:4px}
.stat-image div{width:100%;height:100%}
.stat p{font-size:11.5px;line-height:13.8px;color:var(--ink-soft);padding:8px 4px 0}
.s1{background:linear-gradient(135deg,#eef2f6,#a9bcd3 60%,#6c86a8)}
.s2{background:linear-gradient(135deg,#1b2d4a,#2a4a78 55%,#15233a)}
.s3{background:linear-gradient(135deg,#d9c6a0,#b08948 55%,#6b4e22)}
.s4{background:linear-gradient(135deg,#f2f2f2,#c2c9d0 55%,#7d8791)}
.s5{background:linear-gradient(135deg,#f0f0ef,#cfd1d3 55%,#a4a8ab)}

.footer-note{position:absolute;left:141px;top:777px;width:918px;text-align:center;font-size:11.5px;font-weight:700;line-height:14px;color:var(--ink-soft)}
.legal{position:absolute;left:155px;top:828px;width:890px;text-align:center;font-size:9.8px;font-style:italic;line-height:12.6px;color:#3a3a3a}
</style>
</head>
<body>
<div class="backdrop" role="img" aria-label="Soft grey world map backdrop"></div>

<div class="brand"><span class="brand-name">Tern Harbor</span></div>

<div class="contact-tab">
  <span><svg width="16" height="14" viewBox="0 0 16 14"><path d="M3 1l3 3-2 2c1 2 3 4 5 5l2-2 3 3-2 2C7 13 1 7 1 3z" fill="#333"/></svg>(+44) 01632.960.417</span>
  <span><svg width="16" height="12" viewBox="0 0 16 12"><rect x="1" y="1" width="14" height="10" rx="1" fill="#333"/><path d="M1 2l7 5 7-5" stroke="#dfe3e4" stroke-width="1.4" fill="none"/></svg>marketing@ternharbor.com</span>
</div>

<nav class="nav">
  <div class="nav-home"><svg width="20" height="17" viewBox="0 0 20 17"><path d="M10 1L1 9h3v7h4v-5h4v5h4V9h3z" fill="#bdbdbd"/></svg></div>
  <div class="nav-links"><a>Login</a><i>|</i><a>Register for free</a><i>|</i><a>Contact us</a><i>|</i><a>Terms &amp; Conditions</a></div>
  <div class="follow">Follow us in <span class="social"></span><span class="social"></span></div>
  <div class="search"><div class="search-field"></div><div class="search-btn">Search</div></div>
</nav>

<section class="hero" role="img" aria-label="Abstract dark red cubic pattern">
  <h1 class="hero-title">A potential return of 23.57 % a year from America’s biggest businesses with the emphasis firmly on capital preservation.</h1>
  <div class="hero-cta">FREE REGISTRATION</div>
</section>

<div class="content"></div>

<aside class="sidebar">
  <ul>
    <li class="active">Home</li>
    <li>The Two Minute Guide</li>
    <li>Current holdings &amp; year to date results</li>
    <li>What's on the Watch list</li>
    <li>Other important statistics</li>
    <li>About the back testing model and the results</li>
    <li>History of all trades</li>
    <li>Your questions answered</li>
    <li>About our fundamental analysis and the Margin of Safety</li>
    <li>About value investing</li>
    <li>The Harlow 1000 and the Marden 500 index</li>
  </ul>
</aside>
<div class="trial">Free trial period: if you would like to monitor our service free of charge for six months, then please complete the registration</div>
<div class="rule-v"></div>

<h2 class="intro-title">A methodical, consistent, highly selective system-driven process for identifying, and investing in, undervalued stocks</h2>
<div class="intro-image"><div role="img" aria-label="Glass office towers against a blue sky"></div></div>
<div class="intro-text">
  <p>The attractions of value investing need no explanation to those who subscribe to the concept. But it's impractical, if not impossible, for the private investor to implement the strategy (using direct holdings as distinct to collective funds) consistently. Although the data may be available, to undertake fundamental analysis regularly, on a reasonable number of stocks, takes a significant amount of time and effort.</p>
  <p>By definition - and depending on where you look and market conditions - undervalued businesses (stocks) are relatively scarce. So where does the value investor begin their search? Which and how many businesses must be scrutinised before one undervalued entity is found? And having identified a stock that's trading at less than its estimated fair value, will that be the case next week or next month? Fundamentals can change for the worse at any time, so without the benefit of regular analysis, how will the value investor know when to disinvest?</p>
  <p class="lead">Those problems - and others - are now solved.Our software produces the quantitative analysis value investors need.</p>
</div>
<div class="rule-h"></div>

<div class="stats">
  <div class="stat"><div class="stat-image"><div class="s1" role="img" aria-label="Desk with printed reports"></div></div><p>Average, annualised compound return over to : 23.57 %</p></div>
  <div class="stat"><div class="stat-image"><div class="s2" role="img" aria-label="Dark blue abstract screen"></div></div><p>So far this year, the portfolio's return is 13.49 %:</p></div>
  <div class="stat"><div class="stat-image"><div class="s3" role="img" aria-label="Stacked coins on paper"></div></div><p>Worst ever annual loss: -1.48 %; best ever annual gain: 69.77 %</p></div>
  <div class="stat"><div class="stat-image"><div class="s4" role="img" aria-label="Calculator and pen on printed sheets"></div></div><p>Average return per trade including losing trades: 24.44 %</p></div>
  <div class="stat"><div class="stat-image"><div class="s5" role="img" aria-label="Pen resting on printed tables"></div></div><p>Maximum number of winning/losing trades in a row: 11/4.</p></div>
</div>

<p class="footer-note">If you have any questions, please e-mail info@ternharbor.co.uk. Although we’re very willing to answer queries about the way we pick stocks, please do keep in mind that as we’re making this service available free of charge initially, we’re not inclined to expend time and energy debating the relative merits of value investing or fundamental analysis. Other than that, fire away!</p>
<p class="legal">This website is published by Tern Harbor Ltd. Registered in England No. 08316275. Registered office: 41 Calder Row London N9 4QT. This website and its content is the copyright of Tern Harbor Ltd - © Tern Harbor Ltd 2011. All rights reserved. Any redistribution or reproduction of part or all of the contents in any form is prohibited other than the following: you may print or download to a local hard disk extracts for your personal and non-commercial use only you may copy the content to individual third parties for their personal use, but only if you acknowledge the website as the source of the material. You may not, except with our express written permission, distribute or commercially exploit the content. Nor may you transmit it or store it in any other website or other form of electronic retrieval system.</p>
</body>
</html>
```